Business Card Design Project

Hello,

We have just created our new COMPANY LOGO via Pixel Harbor and would not like to turn our attention to new Business Cards.

We are a printing company based in Singapore & Las Vegas. We specialize in blue-print printing for the Architectural, Engineering and Construction industries

The design should be simple, professional, clean and organized.

The Business Cards should "pop" when seen and will hopefully be something that makes you look twice.

We have two different Pan-tones that we use for our company, feel free to use them if you think they will work for your design?

Orange: PMS 021
Gray: PMS 431

I have attached our current logo for your use and reference which should obvious be on our business cards.

Considering we have two locations on different continents, we need business cards templates where the address details need to be interchangeable for each different location (total 2)

First one:
38 Merrow Lane #03-11 to #03-15
Singapore 528473
Tel : +65 6847-3920
Fax : +65 6843-7702

Second one:
2381 W. Tanfield Rd, Suite 204
Las Vegas, Nevada 89152
Tel : (702) 555-4137
Fax : (702) 555-4189

We would also like to list a few of our key services on the card. Here are a few examples to get you going.

Plan Printing & Plotting
Digital Colour Printing
Cadline Printing
Specialty Book Making
Scanning & Archiving
Collection & Delivey

This is the first time i have requested for business cards to be created so please let me know if you require any additional information.
Many Thanks,
Tobin
Updates

Project Deadline Extended
Reason: It took us longer than expected to finalize our Company Logo We look forward to receiving your designs.

Target Market(s)

Our Target Market is construction related people.
Construction
Architecture
Engineering

Industry/Entity Type

Printing

Font styles to use
Other font styles liked:
• Times New Roman

Colors
faa54b
ffffff

Requirements
Must have
• The business card must have our Company Logo (attached)
The font used must be Times New Roman
Should not have
• Playful images of print designs and/or logos

```html
<!DOCTYPE html>
<html lang="en">
<head>
<meta charset="utf-8">
<title>Blueline Print Works — Business Card, Front and Back</title>
<link rel="stylesheet" href="https://fonts.googleapis.com/css2?family=Roboto+Condensed:wght@400;700&family=Fira+Sans:wght@300;400&family=Tinos:wght@400&display=swap">
<style>
  :root {
    --stage: #2b2b2c;
    --card-top: #2c2c2e;
    --card-bottom: #111112;
    --orange: #faa54b;
    --orange-deep: #d98a2e;
    --white: #ffffff;
    --soft-white: #e4e4e4;
    --rule: #8a8a8a;
    --gear-gray: #3d3e3c;
  }
  * { margin: 0; padding: 0; box-sizing: border-box; }
  html, body {
    width: 1200px; height: 800px; overflow: hidden;
    background: var(--stage);
  }
  .canvas {
    width: 1200px; height: 800px;
    display: flex; align-items: center; justify-content: center; gap: 30px;
  }
  .card {
    position: relative;
    width: 560px; height: 320px;
    background: linear-gradient(180deg, var(--card-top) 0%, var(--card-bottom) 100%);
    overflow: hidden;
    border-radius: 3px;
    box-shadow: 0 14px 36px rgba(0,0,0,0.45);
  }

  /* Shared brand lockup */
  .brand-mark {
    font-family: "Tinos", "Times New Roman", serif;
    font-weight: 400; color: var(--white);
  }
  .brand-name { display: block; }
  .brand-sub { display: block; color: var(--soft-white); }

  /* Back side */
  .back-gears {
    position: absolute; left: 0; top: 0;
    width: 120px; height: 120px;
    background: linear-gradient(135deg, var(--gear-gray) 0%, rgba(61,62,60,0.25) 100%);
    border-bottom-right-radius: 60px;
  }
  .back .brand-mark {
    position: absolute; left: 0; right: 0; top: 70px;
    text-align: center;
  }
  .back .brand-name { font-size: 24px; }
  .back .brand-sub { font-size: 10px; margin-top: 4px; }
  .services {
    position: absolute; left: 110px; top: 160px;
    display: grid; grid-template-columns: 190px 190px;
    row-gap: 12px; column-gap: 30px;
    list-style: none;
    font-family: "Fira Sans", sans-serif; font-weight: 300;
    font-size: 13px; color: var(--soft-white);
  }
  .service { display: flex; align-items: center; gap: 8px; white-space: nowrap; }
  .service::before {
    content: ""; flex: none;
    width: 8px; height: 8px; border-radius: 50%;
    background: var(--orange);
    box-shadow: 0 0 0 1.5px var(--card-bottom), 0 0 0 2.5px var(--orange);
  }

  /* Front side */
  .wrench-art {
    position: absolute; left: 0; top: 70px;
    width: 100px; height: 250px;
    background: linear-gradient(160deg, var(--orange) 0%, var(--orange-deep) 100%);
    border-top-right-radius: 50px;
  }
  .gear-art {
    position: absolute; right: 0; top: 115px;
    width: 80px; height: 205px;
    background: linear-gradient(180deg, rgba(61,62,60,0.35) 0%, var(--gear-gray) 100%);
    border-top-left-radius: 40px;
  }
  .front .brand-mark {
    position: absolute; right: 18px; top: 16px;
    text-align: center;
  }
  .front .brand-name { font-size: 13px; }
  .front .brand-sub { font-size: 6.5px; margin-top: 2px; }
  .headline { position: absolute; left: 172px; top: 62px; }
  .company-name {
    font-family: "Roboto Condensed", sans-serif;
    font-weight: 700; font-size: 26px; line-height: 1.15;
    color: var(--white);
  }
  .headline-rule { width: 160px; height: 1px; background: var(--rule); margin: 6px 0 5px; }
  .tagline {
    font-family: "Roboto Condensed", sans-serif;
    font-size: 9.5px; color: var(--soft-white);
  }
  .contact {
    position: absolute; left: 180px; top: 190px;
    font-family: "Fira Sans", sans-serif;
    font-size: 11.5px; color: var(--soft-white);
  }
  .contact-row { display: flex; align-items: flex-start; gap: 9px; }
  .contact-row svg { flex: none; margin-top: 2px; }
  .contact-rule { width: 86px; height: 1px; background: var(--rule); margin: 5px 0 5px 36px; }
  .address { line-height: 1.3; }
</style>
</head>
<body>
<main class="canvas">
  <article class="card back">
    <div class="back-gears" role="img" aria-label="Faint gray interlocking gears decoration"></div>
    <div class="brand-mark">
      <span class="brand-name">Blueline Print Works</span>
      <span class="brand-sub">A Member of the BPW Group of Companies</span>
    </div>
    <ul class="services">
      <li class="service">Plan Printing &amp; Plotting</li>
      <li class="service">Digital Colour Printing</li>
      <li class="service">Cadline Printing</li>
      <li class="service">Specialty Book Making</li>
      <li class="service">Scanning &amp; Archiving</li>
      <li class="service">Collection &amp; Delivery</li>
    </ul>
  </article>

  <article class="card front">
    <div class="wrench-art" role="img" aria-label="Orange wrench holding a gear illustration"></div>
    <div class="gear-art" role="img" aria-label="Faint gray interlocking gears decoration"></div>

    <div class="brand-mark">
      <span class="brand-name">Blueline Print Works</span>
      <span class="brand-sub">A Member of the BPW Group of Companies</span>
    </div>

    <header class="headline">
      <h1 class="company-name">Blueline Print<br>Works</h1>
      <div class="headline-rule"></div>
      <p class="tagline">A member of the BPW Group of Companies</p>
    </header>

    <section class="contact">
      <div class="contact-row">
        <svg width="12" height="12" viewBox="0 0 24 24" aria-hidden="true">
          <path fill="var(--orange)" d="M6.6 10.8a15.1 15.1 0 0 0 6.6 6.6l2.2-2.2a1 1 0 0 1 1-.25 11.4 11.4 0 0 0 3.6.57 1 1 0 0 1 1 1V20a1 1 0 0 1-1 1A17 17 0 0 1 3 4a1 1 0 0 1 1-1h3.5a1 1 0 0 1 1 1c0 1.25.2 2.45.57 3.57a1 1 0 0 1-.25 1z"/>
        </svg>
        <span>(702) 555-4137</span>
      </div>
      <div class="contact-rule"></div>
      <div class="contact-row">
        <svg width="12" height="12" viewBox="0 0 24 24" aria-hidden="true">
          <rect x="3" y="8" width="18" height="13" rx="2" fill="var(--orange)"/>
          <rect x="7" y="3" width="10" height="7" fill="var(--orange)"/>
          <rect x="7" y="14" width="10" height="2" fill="var(--card-bottom)"/>
        </svg>
        <span>(702) 555-4189</span>
      </div>
      <div class="contact-rule"></div>
      <div class="contact-row">
        <svg width="12" height="15" viewBox="0 0 24 30" aria-hidden="true">
          <path fill="var(--orange)" d="M12 0a10 10 0 0 0-10 10c0 7.5 10 20 10 20s10-12.5 10-20A10 10 0 0 0 12 0zm0 14a4 4 0 1 1 0-8 4 4 0 0 1 0 8z"/>
        </svg>
        <p class="address">2381 W. Tanfield Rd, Suite 204<br>Las Vegas, Nevada 89152</p>
      </div>
    </section>
  </article>
</main>
</body>
</html>
```